Business card for utility of the future

I need a business card template designed for brookvane. We provide sustainable water, energy and waste services to homes.

The card should include name, position, email address, phone number, website and our logo (attached). I would like it to convey professionalism and creativity.

Target Market(s)

Homeowners, investors, corporate partners.

Industry/Entity Type

Utility

Contact Information for Business Card

The card should include name, position, email address, phone number, website and our logo (attached).

```html
<!DOCTYPE html>
<html lang="en">
<head>
<meta charset="utf-8">
<title>brookvane business card</title>
<link rel="stylesheet" href="https://fonts.googleapis.com/css2?family=Cabin:wght@600;700&display=swap">
<style>
  :root {
    --page: #ffffff;
    --page-edge: #c9c9c9;
    --green-deep: #3c6517;
    --green-mid: #5f8f2e;
    --green-light: #9cc764;
    --ink: #ffffff;
  }
  html, body {
    margin: 0;
    padding: 0;
    width: 1200px;
    height: 1200px;
    overflow: hidden;
    background: var(--page);
  }
  .canvas {
    position: relative;
    width: 1200px;
    height: 1200px;
    box-sizing: border-box;
    border: 1px solid var(--page-edge);
    font-family: "Cabin", "Gill Sans", sans-serif;
  }
  .card {
    position: absolute;
    left: 202px;
    width: 796px;
    height: 461px;
    display: block;
  }
  .card--front { top: 121px; }
  .card--back { top: 618px; }
  .wordmark { font-weight: 700; fill: var(--ink); }
  .wordmark--reflection { opacity: 0.3; }
  .person-name { font-weight: 700; fill: var(--ink); font-size: 80px; }
  .person-role { font-weight: 700; fill: var(--ink); font-size: 32px; }
  .person-phone { font-weight: 700; fill: var(--ink); font-size: 44px; letter-spacing: 2px; }
  .person-email { font-weight: 700; fill: var(--ink); font-size: 27px; }
  .site-url { font-weight: 700; fill: var(--ink); font-size: 26px; }
</style>
</head>
<body>
<div class="canvas">

  <svg class="card card--front" viewBox="0 0 796 461" xmlns="http://www.w3.org/2000/svg">
    <defs>
      <radialGradient id="front-wash" cx="0.55" cy="0.9" r="0.8">
        <stop offset="0" stop-color="var(--green-light)"/>
        <stop offset="0.5" stop-color="var(--green-mid)"/>
        <stop offset="1" stop-color="var(--green-deep)"/>
      </radialGradient>
    </defs>
    <rect width="796" height="461" fill="url(#front-wash)" role="img" aria-label="Photograph of water droplets on green glass"/>
    <text class="wordmark" x="400" y="271" text-anchor="middle" font-size="126">brookvane</text>
    <text class="wordmark wordmark--reflection" x="400" y="-327" text-anchor="middle" font-size="126" transform="scale(1,-1)">brookvane</text>
  </svg>

  <svg class="card card--back" viewBox="0 0 796 461" xmlns="http://www.w3.org/2000/svg">
    <defs>
      <radialGradient id="back-wash" cx="0.5" cy="0.6" r="0.8">
        <stop offset="0" stop-color="var(--green-light)"/>
        <stop offset="0.5" stop-color="var(--green-mid)"/>
        <stop offset="1" stop-color="var(--green-deep)"/>
      </radialGradient>
    </defs>
    <rect width="796" height="461" fill="url(#back-wash)" role="img" aria-label="Photograph of water droplets on green glass"/>
    <text class="person-name" x="380" y="96" text-anchor="middle">Jane Doe</text>
    <text class="person-role" x="380" y="141" text-anchor="middle">Sales Executive</text>
    <text class="person-phone" x="380" y="186" text-anchor="middle">+14 15 555 0193</text>
    <text class="person-email" x="380" y="225" text-anchor="middle">janed@brookvane.com</text>
    <text class="site-url" x="64" y="392">www.brookvane.com</text>
    <text class="wordmark" x="732" y="402" text-anchor="end" font-size="66">brookvane</text>
  </svg>

</div>
</body>
</html>
```